Redesign Event Flyer for Speaker

We are re-designing our professional event flyer template with new headshot and cleaner, up-to-date design. All design details are in PDF file attached. Thank you for participating :)

Font styles to use
Sans Serif

Colors
3276b5
0355a3

Requirements
Must have
• All elements in PDF file.
Nice to have
Should not have
• Tacky or childish elements.

```html
<!DOCTYPE html>
<html lang="en">
<head>
<meta charset="utf-8">
<title>The Greatest Sale – Event Flyer</title>
<link rel="stylesheet" href="https://fonts.googleapis.com/css2?family=Bebas+Neue&family=Cinzel:wght@500&family=Raleway:wght@400;600&display=swap">
<style>
  :root {
    --bg-dark: #2c2c2e;
    --bg-mid: #4a4a4d;
    --bg-light: #6e6e71;
    --white: #ffffff;
    --soft-white: #e6e6e8;
    --brand-red: #e21f26;
    --panel: rgba(30, 30, 32, 0.55);
    --suit-navy: #1d2f57;
    --suit-deep: #14213f;
    --skin-warm: #7a4b35;
  }
  html, body {
    margin: 0;
    padding: 0;
    width: 1200px;
    height: 1028px;
    overflow: hidden;
    background: var(--bg-dark);
  }
  .flyer {
    position: relative;
    width: 1200px;
    height: 1028px;
    overflow: hidden;
    background:
      radial-gradient(ellipse 70% 60% at 62% 48%, var(--bg-light) 0%, var(--bg-mid) 45%, var(--bg-dark) 100%);
    font-family: "Raleway", sans-serif;
    color: var(--white);
  }
  .speaker-photo {
    position: absolute;
    left: 0;
    top: 175px;
    width: 700px;
    height: 853px;
    border-radius: 260px 260px 0 0;
    background:
      radial-gradient(ellipse 26% 20% at 45% 18%, var(--skin-warm) 0%, rgba(122,75,53,0) 100%),
      linear-gradient(180deg, rgba(29,47,87,0) 0%, var(--suit-navy) 38%, var(--suit-deep) 100%);
  }
  .sponsor {
    position: absolute;
    left: 560px;
    top: 88px;
    width: 460px;
    display: flex;
    align-items: center;
    justify-content: center;
    gap: 16px;
  }
  .sponsor-mark {
    width: 44px;
    height: 44px;
    background: var(--brand-red);
  }
  .sponsor-name {
    font-family: "Raleway", sans-serif;
    font-weight: 600;
    font-size: 58px;
    line-height: 1;
    color: var(--brand-red);
  }
  .headline {
    position: absolute;
    left: 395px;
    width: 790px;
    top: 170px;
    margin: 0;
    text-align: center;
    font-family: "Bebas Neue", sans-serif;
    font-weight: 400;
    font-size: 146px;
    line-height: 118px;
    letter-spacing: 1px;
    color: var(--white);
  }
  .headline-rule {
    position: absolute;
    left: 395px;
    top: 425px;
    width: 805px;
    height: 2px;
    background: var(--soft-white);
  }
  .speaker-name {
    position: absolute;
    left: 395px;
    width: 790px;
    top: 440px;
    margin: 0;
    text-align: center;
    font-family: "Cinzel", serif;
    font-weight: 500;
    font-size: 32px;
    letter-spacing: 1px;
    color: var(--soft-white);
  }
  .event-panel {
    position: absolute;
    left: 707px;
    top: 763px;
    width: 493px;
    height: 170px;
    background: var(--panel);
  }
  .event-date {
    position: absolute;
    left: 0;
    width: 493px;
    top: 14px;
    text-align: center;
    font-size: 21px;
    letter-spacing: 1px;
    color: var(--soft-white);
  }
  .panel-rule {
    position: absolute;
    left: 30px;
    width: 440px;
    height: 1px;
    background: var(--soft-white);
  }
  .panel-rule.top { top: 44px; }
  .panel-rule.bottom { top: 125px; }
  .venue {
    position: absolute;
    left: 30px;
    top: 52px;
    height: 66px;
    display: flex;
    align-items: center;
  }
  .venue-id {
    display: flex;
    align-items: center;
    gap: 10px;
    padding-right: 12px;
    border-right: 2px solid var(--soft-white);
  }
  .venue-mark {
    width: 36px;
    height: 36px;
    border: 0;
    background: var(--soft-white);
  }
  .venue-name {
    font-weight: 600;
    font-size: 30px;
    line-height: 1;
    color: var(--white);
  }
  .venue-address {
    padding-left: 12px;
    font-size: 19px;
    line-height: 25px;
    color: var(--soft-white);
  }
  .event-links {
    position: absolute;
    left: 0;
    width: 493px;
    top: 134px;
    text-align: center;
    font-size: 20px;
    color: var(--soft-white);
  }
</style>
</head>
<body>
  <main class="flyer">
    <div class="speaker-photo" role="img" aria-label="Headshot of the speaker in a navy suit and white shirt, smiling"></div>

    <div class="sponsor">
      <span class="sponsor-mark"></span>
      <span class="sponsor-name">Brightpost</span>
    </div>

    <h1 class="headline">The<br>Greatest Sale</h1>
    <div class="headline-rule"></div>
    <p class="speaker-name">Daniel Marcus Hale</p>

    <section class="event-panel">
      <div class="event-date">Friday, August 9th, 2019</div>
      <div class="panel-rule top"></div>
      <div class="venue">
        <div class="venue-id">
          <span class="venue-mark"></span>
          <span class="venue-name">CFGC</span>
        </div>
        <div class="venue-address">4200 Riverside Pkwy,<br>Lakeport, Canada</div>
      </div>
      <div class="panel-rule bottom"></div>
      <div class="event-links">danielmarcushale.com | brightpost.ca</div>
    </section>
  </main>
</body>
</html>
```